Medida Certa - Working hours register App needs interface design

Medida Certa, a 1 million users Brazilian website focused on general calculations needs an interface to an App for registering the working hours of a housemaid, a nanny, a housekeeper or other domestic workers.
The final users should be mainly housewifes.
The wireframe of the pages is in the LarPonto_layout.xls file attached.
Logo is also available in the wireframe.
The interface should be optimized for Android on Orbita KX with a 5'' screen.
Target Market(s)
Females, educated, from 30 to 50 y.o.
Industry/Entity Type
Android
Look and feel
Each slider illustrates characteristics of the customer's brand and the style your logo design should communicate.

```html
<!DOCTYPE html>
<html lang="pt">
<head>
<meta charset="utf-8">
<title>Medida Certa – Registro de ponto</title>
<link rel="stylesheet" href="https://fonts.googleapis.com/css2?family=Arimo:wght@400;700&display=swap">
<style>
  :root {
    --bg: #f4f4f4;
    --header-dark: #2a1414;
    --header-mid: #4a2020;
    --brand-red: #c4161c;
    --profile: #6b3434;
    --strip: #8e2f2f;
    --strip-dark: #6f2424;
    --panel: #dcdcdc;
    --panel-alt: #cfcfcf;
    --hour-bg: #f3f3f3;
    --text-dark: #333;
    --text-mid: #444;
    --green: #8cc13f;
    --green-dark: #6a9a26;
    --dialog: rgba(70, 70, 70, 0.93);
    --dialog-line: rgba(255,255,255,0.14);
    --tick: #2db13a;
    --arrow: #e8141b;
    --white: #fff;
  }
  * { box-sizing: border-box; margin: 0; padding: 0; }
  html, body { width: 1200px; height: 1000px; overflow: hidden; }
  body { background: var(--bg); font-family: "Arimo", Arial, sans-serif; position: relative; }

  .screen { position: absolute; top: 108px; width: 432px; height: 758px; overflow: hidden; background: var(--panel); }
  .screen--main { left: 62px; }
  .screen--dialog { left: 698px; }
  .screen__content { position: absolute; inset: 0; }
  .screen--dialog .screen__content { filter: blur(2px) brightness(0.5); }

  .app-header { position: absolute; left: 0; top: 0; width: 432px; height: 72px;
    background: linear-gradient(90deg, var(--header-dark), var(--header-mid) 50%, var(--header-dark)); }
  .brand-square { position: absolute; left: 6px; top: 8px; width: 66px; height: 54px; background: var(--brand-red); border-radius: 6px; }
  .brand-name { position: absolute; right: 14px; top: 14px; color: var(--white); font-weight: 700; font-size: 34px; }
  .brand-tagline { position: absolute; right: 16px; top: 50px; color: var(--white); font-size: 11px; }

  .profile { position: absolute; left: 0; top: 72px; width: 432px; height: 120px; background: var(--profile); border-top: 3px solid #9a4a4a; }
  .profile__photo { position: absolute; left: 16px; top: 10px; width: 97px; height: 95px; border: 3px solid #eee;
    background: linear-gradient(160deg, #9a9a9a, #3c3c3c); }
  .profile__name { position: absolute; left: 130px; top: 46px; color: var(--white); font-size: 23px; }

  .side-strip { position: absolute; left: 0; top: 192px; width: 123px; height: 500px;
    background: linear-gradient(90deg, var(--strip) 0 40px, var(--strip-dark) 40px 90px, var(--strip) 90px); }
  .clock { position: absolute; left: 28px; top: 78px; }
  .punch-button { position: absolute; left: 4px; top: 203px; width: 110px; height: 58px; border-radius: 6px;
    background: linear-gradient(var(--green), var(--green-dark)); color: var(--white); text-align: center; line-height: 1; }
  .punch-button__small { display: block; font-size: 17px; padding-top: 6px; }
  .punch-button__big { display: block; font-size: 30px; }

  .info { position: absolute; left: 123px; top: 192px; width: 309px; height: 500px; background: var(--panel); color: var(--text-mid); font-size: 14px; }
  .info-row { position: absolute; left: 0; width: 100%; display: flex; justify-content: space-between; padding: 0 14px; }
  .info-row--shade { background: var(--panel-alt); }
  .hour-box { position: absolute; left: 0; top: 70px; width: 100%; height: 118px; background: var(--hour-bg);
    box-shadow: 0 3px 8px rgba(0,0,0,0.35); display: flex; justify-content: space-between; align-items: center; padding: 0 24px 0 16px; font-size: 28px; color: var(--text-dark); }
  .hour-box__label { font-weight: 700; }
  .divider { position: absolute; left: 0; width: 100%; border-top: 2px solid #aaa; }
  .report-title { position: absolute; left: 14px; top: 326px; font-weight: 700; font-size: 13px; text-decoration: underline; }
  .report .info-row { font-size: 13px; }

  .app-footer { position: absolute; left: 0; top: 692px; width: 432px; height: 66px;
    background: linear-gradient(90deg, var(--header-dark), var(--header-mid) 50%, var(--header-dark)); border-top: 3px solid #eee; }
  .footer-icon { position: absolute; top: 10px; width: 46px; height: 44px; background: #e8e8e8; border-radius: 4px; }
  .footer-icon--home { left: 8px; }
  .footer-icon--edit { right: 12px; }

  .dialog { position: absolute; left: 36px; top: 82px; width: 364px; height: 602px; background: var(--dialog); border-radius: 6px; overflow: hidden; color: var(--white); }
  .option { position: absolute; left: 9px; display: flex; align-items: center; font-size: 19px; }
  .option__box { position: relative; width: 34px; height: 34px; border: 2px solid #ddd; margin-right: 10px; }
  .option__box svg { position: absolute; left: 2px; top: -12px; }
  .action { position: absolute; left: 0; width: 100%; display: flex; align-items: center; justify-content: center; font-size: 24px; border-top: 1px solid var(--dialog-line); }
  .action--top { background: rgba(255,255,255,0.05); }

  .flow-arrow { position: absolute; left: 560px; top: 440px; }
</style>
</head>
<body>

<!-- Main screen -->
<section class="screen screen--main">
  <div class="screen__content">
    <header class="app-header">
      <div class="brand-square"></div>
      <div class="brand-name">Medida Certa</div>
      <div class="brand-tagline">Aplicação mobile</div>
    </header>
    <div class="profile">
      <div class="profile__photo" role="img" aria-label="Foto de perfil da funcionária"></div>
      <div class="profile__name">Marta Ribeiro Lins</div>
    </div>
    <aside class="side-strip">
      <svg class="clock" width="100" height="100" viewBox="0 0 100 100">
        <circle cx="50" cy="50" r="48" fill="#ddd" stroke="#999" stroke-width="3"/>
        <circle cx="50" cy="50" r="41" fill="#fff"/>
        <line x1="50" y1="50" x2="50" y2="28" stroke="#222" stroke-width="3"/>
        <line x1="50" y1="50" x2="22" y2="44" stroke="#222" stroke-width="2.5"/>
        <line x1="50" y1="50" x2="66" y2="32" stroke="#c00" stroke-width="1"/>
        <circle cx="50" cy="50" r="3" fill="#222"/>
      </svg>
      <div class="punch-button"><span class="punch-button__small">Punch in</span><span class="punch-button__big">TIME</span></div>
    </aside>
    <div class="info">
      <div class="info-row info-row--shade" style="top:10px;height:36px;padding-top:2px;flex-direction:column;">
        <div style="display:flex;justify-content:space-between;"><span>Date</span><span>25 de Janeiro 2013</span></div>
        <div style="display:flex;justify-content:space-between;"><span>Week Day</span><span>Tuesday</span></div>
      </div>
      <div class="hour-box"><span class="hour-box__label">Hour:</span><span>09:31:31</span></div>
      <div class="info-row info-row--shade" style="top:198px;height:26px;line-height:26px;"><span>Arrival</span><span>08:00</span></div>
      <div class="info-row" style="top:226px;height:28px;line-height:28px;"><span>Lunch Break Start</span><span>00:30</span></div>
      <div class="info-row info-row--shade" style="top:256px;height:28px;line-height:28px;"><span>Lunch Break End</span><span>00:00</span></div>
      <div class="info-row" style="top:287px;height:28px;line-height:28px;"><span>Out</span><span>00:00</span></div>
      <div class="divider" style="top:318px;"></div>
      <div class="report-title">Employe Monthly Report</div>
      <div class="report">
        <div class="info-row info-row--shade" style="top:364px;"><span>Working Hours</span><span>08:00</span></div>
        <div class="info-row" style="top:382px;"><span>Compensated Hour</span><span>00:30</span></div>
        <div class="info-row info-row--shade" style="top:400px;"><span>Extra Hours</span><span>00:00</span></div>
        <div class="info-row" style="top:418px;"><span>Day Extra Hours</span><span>00:00</span></div>
        <div class="info-row info-row--shade" style="top:434px;"><span>Night Extra Hours</span><span>00:00</span></div>
        <div class="info-row" style="top:452px;"><span>Days Absent</span><span></span></div>
      </div>
    </div>
    <footer class="app-footer">
      <svg class="footer-icon footer-icon--home" viewBox="0 0 46 44"><path d="M9 22 L23 9 L37 22 M13 20 V35 H20 V27 H26 V35 H33 V20" fill="none" stroke="#333" stroke-width="3.5"/></svg>
      <svg class="footer-icon footer-icon--edit" viewBox="0 0 46 44"><path d="M12 34 L14 27 L31 10 L36 15 L19 32 Z" fill="#555"/></svg>
    </footer>
  </div>
</section>

<svg class="flow-arrow" width="68" height="46" viewBox="0 0 68 46"><path d="M0 14 H36 V0 L68 23 L36 46 V32 H0 Z" fill="var(--arrow)"/></svg>

<!-- Punch options screen -->
<section class="screen screen--dialog">
  <div class="screen__content">
    <header class="app-header">
      <div class="brand-square"></div>
      <div class="brand-name">Medida Certa</div>
      <div class="brand-tagline">Aplicação mobile</div>
    </header>
    <div class="profile">
      <div class="profile__photo" role="img" aria-label="Foto de perfil da funcionária"></div>
      <div class="profile__name">Marta Ribeiro Lins</div>
    </div>
    <aside class="side-strip">
      <div class="punch-button"><span class="punch-button__small">Punch in</span><span class="punch-button__big">TIME</span></div>
    </aside>
    <div class="info">
      <div class="hour-box"><span class="hour-box__label">Hour:</span><span>09:31:31</span></div>
    </div>
    <footer class="app-footer"></footer>
  </div>

  <div class="dialog">
    <div class="option" style="top:6px;"><span class="option__box"><svg width="44" height="40" viewBox="0 0 44 40"><path d="M2 24 L14 36 L42 4" fill="none" stroke="var(--tick)" stroke-width="7"/></svg></span>Late arrival?</div>
    <div class="option" style="top:62px;"><span class="option__box"></span>Sooner than expected leave?</div>
    <div class="option" style="top:115px;"><span class="option__box"></span>Option 3?</div>
    <div class="option" style="top:169px;"><span class="option__box"><svg width="44" height="40" viewBox="0 0 44 40"><path d="M2 24 L14 36 L42 4" fill="none" stroke="var(--tick)" stroke-width="7"/></svg></span>Option 4?</div>
    <div class="option" style="top:222px;"><span class="option__box"></span>Option 5?</div>
    <div class="action action--top" style="top:265px;height:88px;">Punch in arrival.</div>
    <div class="action" style="top:353px;height:87px;">Punch in Lunch Break Start</div>
    <div class="action" style="top:440px;height:88px;">Punch in Lunch Break End</div>
    <div class="action" style="top:528px;height:74px;">Punch in Out.</div>
  </div>
</section>

</body>
</html>
```